Silverpine Orbit Works Flyer

We need a one page promotional piece that explains what our company does, and the benefits it provides in a simple, elegant, easy to understand way. I would like to print it on glossy heavyweight paper to give a feel of high quality and legitimacy. I will include the logo, the tag line, and the main benefits that the company offers.

Tag line concept, may not need these exact words. "Lend us 5 minutes each morning, and we will guide you toward a Silverpine Orbit Works."

Key points...(exact wording not required if you think of a better way to say it)

Software easy enough for my grandpa to use.
Lets you use snail mail, email, texting, and social media to quickly market to your customers at very low cost.
Web based which allows you to launch media campaigns from your desktop, or smartphone in moments.
Quick 3 - 5 minute training videos which give you hard hitting, quick action tips that will help you make your business better today.
Live coaching calls to help motivate you to improve your business.
No contracts, or start up fees. One low price of $299 per month.

Restaurant owners

Restaurant

```html
<!DOCTYPE html>
<html lang="en">
<head>
<meta charset="utf-8">
<title>Silverpine Orbit Works Flyer</title>
<link href="https://fonts.googleapis.com/css2?family=Archivo+Black&family=Arimo:ital,wght@0,700;1,400&family=Cousine&display=swap" rel="stylesheet">
<style>
  :root {
    --sky-top: #bcd2e9;
    --sky-bottom: #93b3da;
    --ink-gray: #5b5b5e;
    --brand-green: #5c9e3b;
    --band-green: #5f9e3e;
    --white: #ffffff;
    --foot-blue: #8eafd7;
  }
  html, body { margin: 0; padding: 0; overflow: hidden; }
  .flyer {
    position: relative;
    width: 849px;
    height: 1200px;
    overflow: hidden;
    background: linear-gradient(180deg, var(--sky-top) 0%, var(--sky-bottom) 78%);
    font-family: "Arimo", Arial, sans-serif;
  }
  .headline {
    position: absolute;
    top: 132px;
    left: 0;
    width: 100%;
    margin: 0;
    text-align: center;
    font-family: "Archivo Black", "Arial Black", sans-serif;
    font-weight: 400;
    line-height: 1;
  }
  .headline span { display: block; }
  .headline-top {
    color: var(--ink-gray);
    font-size: 42px;
    letter-spacing: 6px;
  }
  .headline-middle {
    color: var(--brand-green);
    font-size: 82px;
    letter-spacing: 18px;
    margin-top: -2px;
  }
  .headline-bottom {
    color: var(--ink-gray);
    font-size: 64px;
    letter-spacing: 6px;
    margin-top: -10px;
    text-transform: lowercase;
  }
  .hero-illustration {
    position: absolute;
    left: 196px;
    top: 337px;
    width: 441px;
    height: 395px;
    border-radius: 30px;
    background: radial-gradient(ellipse at 55% 60%, #f4f4f4 0%, #c9c9cb 55%, #9ba9bb 100%);
  }
  .tagline {
    position: absolute;
    top: 770px;
    left: 0;
    width: 100%;
    margin: 0;
    text-align: center;
    color: var(--brand-green);
    font-weight: 700;
    font-size: 25px;
    letter-spacing: 2px;
  }
  .offer-terms {
    position: absolute;
    top: 806px;
    left: 0;
    width: 100%;
    margin: 0;
    text-align: center;
    color: var(--brand-green);
    font-style: italic;
    font-weight: 400;
    font-size: 33px;
    letter-spacing: 1px;
  }
  .price {
    position: absolute;
    top: 842px;
    left: 228px;
    margin: 0;
    color: var(--ink-gray);
    font-weight: 700;
    font-size: 56px;
    line-height: 1.1;
  }
  .price-unit { font-size: 28px; }
  .benefits {
    position: absolute;
    top: 939px;
    left: 0;
    width: 100%;
    height: 205px;
    background: var(--band-green);
  }
  .benefits-list {
    list-style: none;
    margin: 0;
    padding: 16px 0 0 135px;
    font-family: "Cousine", "Courier New", monospace;
    font-size: 27px;
    letter-spacing: 0.6px;
    line-height: 34px;
    color: var(--white);
  }
  .footer-strip {
    position: absolute;
    top: 1144px;
    left: 0;
    width: 100%;
    height: 56px;
    background: var(--foot-blue);
  }
</style>
</head>
<body>
  <main class="flyer">
    <h1 class="headline">
      <span class="headline-top">SILVERPINE</span>
      <span class="headline-middle">ORBIT</span>
      <span class="headline-bottom">works</span>
    </h1>

    <div class="hero-illustration" role="img" aria-label="Illustration of a white money bag with a dollar sign, set between a dark gray fork and knife like a dinner plate"></div>

    <p class="tagline">All it takes is 5 minutes a day</p>
    <p class="offer-terms">NO CONTRACTS/ START-UP FEES</p>
    <p class="price">$299/<span class="price-unit">MONTH</span></p>

    <section class="benefits">
      <ul class="benefits-list">
        <li>what you can expect:</li>
        <li>simple software</li>
        <li>diverse marketing</li>
        <li>succinct training videos</li>
        <li>live coaching calls</li>
      </ul>
    </section>

    <div class="footer-strip"></div>
  </main>
</body>
</html>
```